Kalmoret Windham & Associates

We would like a simple, professional business card using a similar font to our logo.

Industry/Entity Type

Law Firm

Contact Information for Business Card

Martin Kalmoret, Esq. 47 Tillman Lane, 2nd Floor Brantwell, MA 02187 Office: 781.555.0143 Cell: 508.555.0196 Email: marty@kwfirmma.com kalmoretwindhamlaw.com

Font styles to use
Other font styles liked:
• We would like to use the fonts used in the logo or similar

Colors
0054AA
0677BA
7BADD7
CADEEF
E8F1F8

Requirements
Must have
• We would like the fonts to match the logo
Nice to have
• not too much design- very simple and professional business card. I added a picture of a business card that I tried to start but I am not a designer! Hopefully it will help with the address and phone numbers and kind of what we are looking for.

```html
<!DOCTYPE html>
<html lang="en">
<head>
<meta charset="utf-8">
<title>Kalmoret Windham &amp; Associates – Business Card</title>
<link rel="stylesheet" href="https://fonts.googleapis.com/css2?family=Crimson+Text:wght@400;600&display=swap">
<style>
  :root {
    --navy: #1f3a72;
    --navy-line: #3b5590;
    --white: #ffffff;
    --grey: #77787c;
    --ink: #2c2c30;
    --backdrop: #e6e7ea;
    --frame: #b9c3d8;
  }
  * { box-sizing: border-box; margin: 0; padding: 0; }
  html, body { width: 1200px; height: 998px; overflow: hidden; }
  body {
    background: var(--backdrop);
    font-family: "Crimson Text", Georgia, serif;
    position: relative;
  }
  .card {
    position: absolute;
    left: 220px;
    width: 760px;
    height: 434px;
    box-shadow: 0 6px 18px rgba(0,0,0,.18);
  }
  .card--front { top: 40px; background: var(--navy); }
  .card--back  { top: 524px; background: var(--white); }

  .lockup { position: absolute; display: flex; align-items: center; }
  .lockup__square { flex: none; }
  .lockup__rule { width: 1px; flex: none; }
  .lockup__name {
    font-weight: 600;
    text-transform: uppercase;
    line-height: 1.02;
    letter-spacing: .02em;
    white-space: nowrap;
  }

  .card--front .lockup { left: 150px; top: 142px; }
  .card--front .lockup__square {
    width: 212px; height: 134px;
    border: 1px solid var(--frame);
  }
  .card--front .lockup__rule { height: 150px; margin: 0 36px 0 44px; background: var(--grey); }
  .card--front .lockup__name { color: var(--white); font-size: 34px; }

  .card--back .lockup { left: 58px; top: 260px; }
  .card--back .lockup__square { width: 140px; height: 92px; background: var(--navy); }
  .card--back .lockup__rule { height: 104px; margin: 0 18px 0 22px; background: var(--grey); }
  .card--back .lockup__name { color: var(--navy); font-size: 22px; }

  .divider {
    position: absolute;
    left: 420px; top: 84px;
    width: 1px; height: 250px;
    background: var(--navy-line);
  }
  .contact { position: absolute; left: 452px; top: 80px; color: var(--ink); }
  .contact__name { color: var(--navy); font-size: 32px; font-weight: 400; line-height: 1.1; margin-bottom: 12px; white-space: nowrap; }
  .contact__address { font-style: normal; font-size: 19px; line-height: 1.2; margin-bottom: 14px; }
  .contact__list { list-style: none; font-size: 19px; line-height: 1.3; }
  .contact__list li { display: flex; align-items: center; gap: 10px; }
  .contact__list svg { width: 16px; height: 16px; flex: none; fill: var(--navy); }
</style>
</head>
<body>

<section class="card card--front" aria-label="Card front">
  <div class="lockup">
    <span class="lockup__square"></span>
    <span class="lockup__rule"></span>
    <p class="lockup__name">Kalmoret<br>Windham<br>&amp; Associates</p>
  </div>
</section>

<section class="card card--back" aria-label="Card back">
  <div class="lockup">
    <span class="lockup__square"></span>
    <span class="lockup__rule"></span>
    <p class="lockup__name">Kalmoret<br>Windham<br>&amp; Associates</p>
  </div>

  <span class="divider"></span>

  <div class="contact">
    <h1 class="contact__name">Martin Kalmoret, Esq.</h1>
    <address class="contact__address">47 Tillman Lane, 2nd Floor<br>Brantwell, MA 02187</address>
    <ul class="contact__list">
      <li>
        <svg viewBox="0 0 16 16" aria-hidden="true"><path d="M1 6c0-2 3-3 7-3s7 1 7 3v1h-3V5.5C11 5 9.5 5 8 5s-3 0-4 .5V7H1zM3 8h10l1 6H2z"/></svg>
        781.555.0143
      </li>
      <li>
        <svg viewBox="0 0 16 16" aria-hidden="true"><path d="M3 1h3l1 4-2 1c1 2 2 3 4 4l1-2 4 1v3c0 1-1 3-3 3C6 15 1 10 1 4c0-2 1-3 2-3z"/></svg>
        508.555.0196
      </li>
      <li>
        <svg viewBox="0 0 16 16" aria-hidden="true"><path d="M1 3h14v10H1zM2 4l6 5 6-5z" fill-rule="evenodd"/></svg>
        marty@kwfirmma.com
      </li>
      <li>
        <svg viewBox="0 0 16 16" aria-hidden="true"><circle cx="8" cy="8" r="7"/><path d="M5 5c2 0 3 1 2 3s1 3 2 5" stroke="#fff" stroke-width="1.2" fill="none"/></svg>
        kalmoretwindhamlaw.com
      </li>
    </ul>
  </div>
</section>

</body>
</html>
```